Private Gym Needs a Rack Card Design

We need a basic front and back rack card (same size as post card) that gives basic information about our brand, and includes our logo. Please see attached logo and required content below.

Target Market(s)

Upscale, private gym.

Industry/Entity Type

Gym

Font styles to use
Sans Serif

Colors
ffffff
5c5c5c
000000
dbdbdb
f78f20

Requirements
Must have
• Business Logo and the following text in a clean, modern, easy-to-read, artistic manner. Style and design must be clean, incorporate our color scheme of MOSTLY white, light grey, charcoal, with just pops of orange. We want the card itself to be mostly white background. Must include website URL as well: corevantagestudio.com
• FRONT CARD:
• Logo
• A safe and individualized approach to exercise
• Our method employs the latest weight resistance training exercises and coaching for healthy living. Not only is our workout methodology effective, it’s safe.
• Our Method…
• -Improves Functional Movement
• -Promotes Weight Loss
• -Builds Strength
• -Increases Flexibility 

• BACK:
• Change Your Body. Find Your Strength.
• There’s 40 years of success behind our proven method
• What is The Formwell? 
• The Formwell is all about teaching our clients how to lift weights and exercise with the proper technique. There’s no slinging or jerking at our gym; only controlled movements that yield real results.
• Come workout with us in our private gym. We are located in Durham adjacent to Harlow Campus and 5 minutes from downtown Durham.
• Address: 482 Linden Ave, Durham, NC 27705
• Phone: (919) 555-2741
• Hours: 9:00 AM – 9:00 PM
Nice to have
• Great organization of text, maybe some columns, colored bullet points, cool graphics and logos.
Should not have
• Busy or crowded design. All lines should be sleek, straight, and streamline. NO STOCK IMAGES, but logos are GREAT

```html
<!DOCTYPE html>
<html lang="en">
<head>
<meta charset="utf-8">
<title>The Formwell – Rack Card Back</title>
<link href="https://fonts.googleapis.com/css2?family=Quicksand:wght@500;600&display=swap" rel="stylesheet">
<style>
  :root {
    --white: #ffffff;
    --ink: #111111;
    --charcoal: #222222;
    --grey: #5c5c5c;
    --orange: #f0673a;
    --amber: #f7931e;
    --peach: #f6ad58;
  }
  html, body { margin: 0; padding: 0; overflow: hidden; background: var(--white); }
  .card {
    position: relative; width: 1200px; height: 857px; overflow: hidden;
    background: var(--white); color: var(--ink);
    font-family: "Quicksand", sans-serif; font-weight: 500;
  }
  .card > * { position: absolute; margin: 0; white-space: nowrap; }

  .brand-mark { left: 6px; top: 30px; width: 130px; color: var(--orange); font-size: 25px; font-weight: 600; line-height: 1.05; }
  .headline { left: 142px; top: 22px; font-size: 56px; color: var(--orange); font-weight: 500; letter-spacing: -0.3px; }
  .tagline { right: 32px; top: 92px; font-size: 30px; }

  .method-title { left: 14px; top: 168px; font-size: 64px; line-height: 1; }
  .method-box {
    left: 62px; top: 250px; width: 630px; height: 383px;
    border: 6px solid var(--amber);
  }
  .method-box p { margin: 0; padding: 14px 0 0 20px; font-size: 41px; line-height: 53px; white-space: nowrap; }

  .bar { position: absolute; }
  .accent-peach { left: 902px; top: 166px; width: 298px; height: 56px; background: var(--peach); }
  .accent-black-1 { left: 1038px; top: 240px; width: 162px; height: 45px; background: var(--charcoal); }
  .accent-orange { left: 913px; top: 308px; width: 287px; height: 23px; background: var(--orange); }
  .accent-black-2 { left: 982px; top: 352px; width: 218px; height: 50px; background: var(--charcoal); }
  .accent-grey { left: 1034px; top: 424px; width: 166px; height: 48px; background: var(--grey); }

  .website { left: 858px; top: 558px; width: 342px; height: 31px; background: var(--orange); color: var(--white); font-size: 24px; line-height: 31px; text-align: center; }
  .contact { left: 841px; top: 589px; width: 347px; height: 85px; padding-left: 12px; background: var(--peach); font-size: 26px; line-height: 34px; padding-top: 9px; box-sizing: border-box; letter-spacing: -0.5px; }

  .location { left: 456px; top: 674px; width: 744px; height: 143px; box-sizing: border-box; padding: 8px 0 0 17px; background: var(--grey); color: var(--white); font-size: 26px; line-height: 33px; }
  .location p { margin: 0; }

  .chart-bars { left: 0; top: 0; width: 1200px; height: 857px; pointer-events: none; }
</style>
</head>
<body>
<main class="card">
  <div class="brand-mark">The<br>Formwell</div>
  <h1 class="headline">Change Your Body. Find Your Strength.</h1>
  <p class="tagline">There’s 40 years of success behind our proven method</p>

  <h2 class="method-title">What is The Formwell?</h2>
  <div class="method-box">
    <p>&nbsp;It is all about teaching our<br>clients how to lift weights<br>and exercise with the proper<br>technique. There’s no slinging<br>&nbsp;or jerking at our gym; only<br>&nbsp;controlled movements that<br>&nbsp;yield real results.</p>
  </div>

  <div class="bar accent-peach"></div>
  <div class="bar accent-black-1"></div>
  <div class="bar accent-orange"></div>
  <div class="bar accent-black-2"></div>
  <div class="bar accent-grey"></div>

  <div class="website">corevantagestudio.com</div>
  <div class="contact">- Phone: (919) 555-2741<br>- Hours: 9:00 AM – 9:00 PM</div>

  <div class="location">
    <p>Come workout with us in our private gym.</p>
    <p>We are located in Durham adjacent to Harlow</p>
    <p>Campus and 5 minutes from downtown Durham.</p>
    <p>- Address: 482 Linden Ave, Durham, NC 27705</p>
  </div>

  <svg class="chart-bars" viewBox="0 0 1200 857" aria-hidden="true">
    <rect x="28" y="748" width="40" height="109" fill="#5c5c5c"/>
    <rect x="78" y="701" width="48" height="156" fill="#222222"/>
    <rect x="140" y="736" width="26" height="121" fill="#f6ad58"/>
    <rect x="185" y="715" width="50" height="142" fill="#222222"/>
    <rect x="250" y="669" width="44" height="188" fill="#5c5c5c"/>
    <rect x="304" y="742" width="40" height="115" fill="#f0673a"/>
  </svg>
</main>
</body>
</html>
```